Letter Head, for use on daily correspondence with other companies

Hi

I want a professional Letter head, That my company can use to corresponded with other companies we do business with on a daily basis.

I want this done as soon as possible as this is peak session for us.

I have attached the company logo so please be creative and professional.
Kind regards

Marcus

Target Market(s)

All Audience searching for tickets, people in the entertainment world

Industry/Entity Type

Entertainment Industry

Font styles to use
Serif
Sans Serif
Decorative
Script

Requirements
Must have
• Very professional image.
• I will know want i want when i see it
• so please do your utmost in your professional standards
• Address of the company 24 hollin lane, telephone number 0207 562 3198
• Vat number: 487 2915 06.
• This letter head my be able to acomodate usage for directors & CEO as well as managers and employess
Nice to have
• A great professional image
Should not have
• Be creative please

```html
<!DOCTYPE html>
<html lang="en">
<head>
<meta charset="utf-8">
<title>Seatly Letterhead</title>
<link href="https://fonts.googleapis.com/css2?family=Carlito:wght@400;700&display=swap" rel="stylesheet">
<style>
  :root {
    --backdrop: #4a4b50;
    --paper: #f7f7f7;
    --ink: #111111;
    --brand-red: #cc2200;
    --brand-red-light: #e0522e;
    --paper-white: #ffffff;
  }
  * { margin: 0; padding: 0; box-sizing: border-box; }
  html, body {
    width: 1200px; height: 1000px; overflow: hidden;
    background: var(--backdrop);
    font-family: "Carlito", "Calibri", sans-serif;
  }
  .letterhead {
    position: absolute; left: 352px; top: 113px;
    width: 500px; height: 708px;
    background: var(--paper);
  }
  .brand-block {
    position: absolute; left: 408px; top: 43px;
    width: 92px; height: 66px;
    background: var(--brand-red);
    border-bottom: 2px solid var(--brand-red-light);
    display: flex; align-items: center; justify-content: center;
  }
  .brand-name {
    color: var(--paper-white);
    font-size: 22px; font-weight: 700; letter-spacing: 0.5px;
  }
  .letter-text {
    position: absolute; left: 46px;
    font-size: 11px; line-height: 14px; color: var(--ink);
  }
  .date { top: 142px; }
  .recipient { top: 170px; }
  .salutation { top: 238px; }
  .para-1 { top: 266px; }
  .para-2 { top: 308px; }
  .para-3 { top: 364px; }
  .para-4 { top: 447px; }
  .closing { top: 545px; }
  .signature { top: 586px; }
  .contact-details {
    position: absolute; right: 18px; top: 604px;
    text-align: right; color: var(--brand-red);
    font-size: 10px; font-weight: 700; line-height: 16.5px;
  }
  .contact-strip {
    position: absolute; left: 486px; top: 596px;
    width: 14px; height: 66px;
    background: var(--brand-red);
  }
</style>
</head>
<body>
  <main class="letterhead">
    <div class="brand-block"><span class="brand-name">seatly</span></div>

    <p class="letter-text date">August 28, 2011</p>
    <p class="letter-text recipient">First Last Name<br>Street Address<br>City, State 00000</p>
    <p class="letter-text salutation">Dear :</p>
    <p class="letter-text para-1">Lorem ipsum dolor sit amet, consectetur adipiscing elit. Aenean ut ipsum eget massa<br>hendrerit vestibulum vel in velit. Donec pretium neque velit.</p>
    <p class="letter-text para-2">Aliquam porta lectus nec mauris ornare venenatis. Vivamus non est turpis, et cursus<br>sem. Mauris vehicula erat in diam auctor at bibendum nisl lacinia. Morbi imperdiet<br>neque vehicula nunc convallis gravida. Vestibulum iaculis pretium placerat.</p>
    <p class="letter-text para-3">Integer consequat, est sit amet facilisis eleifend, nibh nibh varius orci, eget dapibus<br>arcu dui non purus. Pellentesque in magna mauris. Duis enim sapien, dictum vitae<br>condimentum a, pulvinar vel lacus. Mauris et nibh. Vestibulum vitae nulla at metus<br>elementum porta sit amet interdum elit. Nulla sollicitudin neque eu nulla volutpat<br>congue.</p>
    <p class="letter-text para-4">Etiam pellentesque, velit id dapibus fermentum, turpis sapien ornare dui, ac tincidunt<br>ligula odio congue purus. Nunc sed ante dui, in porta lectus. Cras nec sem lorem. In hac<br>habitasse platea dictumst. Maecenas id diam quis dui porta tristique. Sed id egestas felis.<br>Donec ullamcorper mattis posuere. Phasellus fermentum eleifend tortor vel dapibus.<br>Vestibulum ante ipsum.</p>
    <p class="letter-text closing">Sincerely,</p>
    <p class="letter-text signature">John Doe</p>

    <address class="contact-details">24 Hollin Lane<br>0207 562 3198<br>487 2915 06</address>
    <svg class="contact-strip" width="14" height="66" viewBox="0 0 14 66" aria-hidden="true">
      <path d="M7 9.5c-1.6 0-2.6 1.1-2.6 2.5 0 1.8 2.6 4.6 2.6 4.6s2.6-2.8 2.6-4.6c0-1.4-1-2.5-2.6-2.5z" fill="#fff"/>
      <circle cx="7" cy="12" r="0.9" fill="#cc2200"/>
      <path d="M4.6 29.2c.4-.4.9-.4 1.2 0l.8.9c.3.3.3.7 0 1l-.4.4c.4.8 1 1.4 1.8 1.8l.4-.4c.3-.3.7-.3 1 0l.9.8c.4.3.4.8 0 1.2l-.6.6c-2.2 0-5.6-3.4-5.6-5.6z" fill="#fff"/>
      <text x="7" y="52" text-anchor="middle" font-family="Carlito, sans-serif" font-size="7" font-weight="700" fill="#fff">VAT</text>
    </svg>
  </main>
</body>
</html>
```